B.R. Rimworks / Varro / GlossPeak stationery
Design Engineering and manufacturing
B.R. Rimworks / Varro / GlossPeak stationery - Automotive
Creative Brief
Professional
Daniel Pruitt
Managing Member
4837 58th Ct W Sarasota, FL 34251
DanielPruitt@brrimworks.example
www.BRrimworksLLC.example
Please put all the logos on the back of the business card

```html
<!DOCTYPE html>
<html lang="en">
<head>
<meta charset="utf-8">
<title>B.R. Rimworks Stationery</title>
<link href="https://fonts.googleapis.com/css2?family=Montserrat:wght@400;700&family=Open+Sans:wght@400;600&display=swap" rel="stylesheet">
<style>
:root{
  --navy:#1d4c8a;
  --navy-dark:#153a6b;
  --silver:#d9dee6;
  --paper:#ffffff;
  --ink:#555b66;
  --stage:#4b4c4f;
}
*{box-sizing:border-box;margin:0;padding:0}
html,body{width:1200px;height:274px;overflow:hidden;background:var(--stage);font-family:"Open Sans",sans-serif;color:var(--ink)}
.board{position:relative;width:1200px;height:274px}
.item{position:absolute;background:var(--paper);box-shadow:0 2px 5px rgba(0,0,0,.45);overflow:hidden}
.brand{display:flex;align-items:center;gap:3px;font-family:"Montserrat",sans-serif;font-weight:700;color:var(--navy);white-space:nowrap}
.brand .dot{border-radius:50%;background:var(--navy);flex:none}
.brand.light{color:var(--paper)}
.brand.light .dot{background:var(--paper)}
.wave{position:absolute;left:0;bottom:0;width:100%;display:block}
.tiny{font-size:3.4px;line-height:4.6px;white-space:nowrap}
.small{font-size:4px;line-height:5.4px}

/* logo block */
.logo-block{position:absolute;left:22px;top:28px;width:160px;height:62px;background:transparent}
.logo-block .brand{font-size:13px;color:var(--paper)}
.logo-block .dot{width:16px;height:16px;background:var(--paper)}
.logo-block .tagline{margin:3px 0 0 19px;font-family:"Montserrat",sans-serif;font-size:6px;color:var(--silver)}

/* letterheads */
.letterhead{top:24px;width:124px;height:236px}
.letterhead .brand{position:absolute;top:12px;left:50%;transform:translateX(-50%);font-size:7px}
.letterhead .brand .dot{width:8px;height:8px}
.letterhead .body{position:absolute;top:42px;left:14px;right:14px}
.letterhead .body p{margin-bottom:4px}
.letterhead .sign{margin-top:8px}

/* business cards */
.card{width:98px;height:56px}
.card .brand{font-size:6px}
.card .brand .dot{width:7px;height:7px}
.card.front .brand{position:absolute;top:8px;left:8px}
.card.front .details{position:absolute;left:8px;top:20px}
.card.front .name{font-family:"Montserrat",sans-serif;font-weight:700;font-size:4.4px;line-height:6px;color:var(--navy)}
.card.back{background:var(--navy)}
.card.back .brand{position:absolute;top:50%;left:50%;transform:translate(-50%,-50%)}
.partner{width:46px;height:26px;display:flex;align-items:center;justify-content:center;font-family:"Montserrat",sans-serif;font-weight:700;font-size:6px;color:var(--navy)}

/* envelopes */
.envelope .brand{position:absolute;top:7px;left:8px;font-size:5px}
.envelope .brand .dot{width:6px;height:6px}
.envelope .stripe{position:absolute;left:0;right:0;height:6px;background:var(--navy)}

/* folder */
.folder{left:816px;top:22px;width:372px;height:238px;background:var(--navy)}
.folder .spine{position:absolute;left:185px;top:0;bottom:0;width:2px;background:var(--navy-dark)}
.folder .pocket{position:absolute;bottom:0;height:96px}
.folder .pocket-left{left:8px;width:170px;background:var(--silver)}
.folder .pocket-right{left:194px;width:170px;background:var(--paper)}
.folder .cover-brand{position:absolute;font-size:12px}
.folder .cover-brand .dot{width:14px;height:14px}
</style>
</head>
<body>
<div class="board">

  <div class="logo-block">
    <div class="brand"><span class="dot"></span>B.R. Rimworks</div>
    <div class="tagline">Professional coverage</div>
  </div>

  <!-- business cards -->
  <div class="item card front" style="left:12px;top:118px">
    <div class="brand"><span class="dot"></span>B.R. Rimworks</div>
    <div class="details tiny">
      <div class="name">Member Name</div>
      <div>Managing Member</div>
      <div>Street Address, City</div>
      <div>mail@brrimworks.example</div>
      <div>brrimworks.example</div>
    </div>
  </div>
  <div class="item card back" style="left:12px;top:180px;height:32px">
    <div class="brand light"><span class="dot"></span>B.R. Rimworks</div>
  </div>
  <div class="item partner" style="left:12px;top:222px">Varro</div>
  <div class="item partner" style="left:64px;top:222px">GlossPeak</div>

  <!-- letterheads -->
  <div class="item letterhead" style="left:259px">
    <div class="brand"><span class="dot"></span>B.R. Rimworks</div>
    <div class="body small">
      <p>Dear Client,</p>
      <p>We design and build custom wheels with care and precision for every vehicle we service.</p>
      <p class="sign">Sincerely,</p>
    </div>
    <svg class="wave" viewBox="0 0 124 40" height="40" preserveAspectRatio="none"><path d="M0 18 Q62 0 124 14 V40 H0Z" fill="var(--silver)"/><path d="M0 26 Q62 10 124 22 V40 H0Z" fill="var(--navy)"/></svg>
  </div>
  <div class="item letterhead" style="left:390px">
    <div class="brand"><span class="dot"></span>B.R. Rimworks</div>
    <div class="body small">
      <p>Dear Client,</p>
      <p>We design and build custom wheels with care and precision for every vehicle we service.</p>
      <p class="sign">Sincerely,</p>
    </div>
    <svg class="wave" viewBox="0 0 124 40" height="40" preserveAspectRatio="none"><path d="M0 18 Q62 0 124 14 V40 H0Z" fill="var(--silver)"/><path d="M0 26 Q62 10 124 22 V40 H0Z" fill="var(--navy)"/></svg>
  </div>

  <!-- middle cards -->
  <div class="item card back" style="left:528px;top:32px;width:76px;height:44px">
    <div class="brand light" style="font-size:5px"><span class="dot" style="width:6px;height:6px"></span>B.R. Rimworks</div>
  </div>
  <div class="item card front" style="left:614px;top:32px;width:72px;height:40px">
    <div class="brand" style="font-size:5px;top:6px;left:6px"><span class="dot" style="width:5px;height:5px"></span>B.R. Rimworks</div>
    <svg class="wave" viewBox="0 0 72 10" height="10" preserveAspectRatio="none"><path d="M0 4 Q36 0 72 3 V10 H0Z" fill="var(--navy)"/></svg>
  </div>

  <!-- small envelopes -->
  <div class="item envelope" style="left:520px;top:108px;width:96px;height:50px">
    <div class="brand"><span class="dot"></span>B.R. Rimworks</div>
    <svg class="wave" viewBox="0 0 96 14" height="14" preserveAspectRatio="none"><path d="M0 6 Q48 0 96 5 V14 H0Z" fill="var(--navy)"/></svg>
  </div>
  <div class="item envelope" style="left:516px;top:172px;width:108px;height:60px">
    <div class="brand"><span class="dot"></span>B.R. Rimworks</div>
    <svg class="wave" viewBox="0 0 108 16" height="16" preserveAspectRatio="none"><path d="M0 7 Q54 0 108 6 V16 H0Z" fill="var(--navy)"/></svg>
  </div>

  <!-- DL envelopes -->
  <div class="item envelope" style="left:690px;top:116px;width:118px;height:44px">
    <div class="brand"><span class="dot"></span>B.R. Rimworks</div>
    <div class="stripe" style="bottom:0"></div>
  </div>
  <div class="item envelope" style="left:690px;top:166px;width:118px;height:34px">
    <svg viewBox="0 0 118 34" width="118" height="34" preserveAspectRatio="none"><path d="M0 0 L59 20 L118 0" fill="none" stroke="var(--silver)" stroke-width="1"/></svg>
    <div class="stripe" style="bottom:0;height:4px"></div>
  </div>
  <div class="item envelope" style="left:690px;top:208px;width:118px;height:44px">
    <div class="stripe" style="top:0"></div>
    <div class="brand" style="top:14px"><span class="dot"></span>B.R. Rimworks</div>
  </div>

  <!-- presentation folder -->
  <div class="item folder">
    <div class="pocket pocket-left"></div>
    <div class="pocket pocket-right"></div>
    <div class="spine"></div>
    <div class="brand light cover-brand" style="left:24px;top:60px"><span class="dot"></span>B.R. Rimworks</div>
    <div class="brand cover-brand" style="left:226px;top:178px;font-size:9px"><span class="dot" style="width:10px;height:10px"></span>B.R. Rimworks</div>
  </div>

</div>
</body>
</html>
```